Plumbing & Heating bussiness card design

i do all plumbing and heating work and need a catchy design. keep it simple but eye catching nothing gimicky
i do 24hr call outs
landlord safety checks
all aspects of plumbing and heating
boiler breakdowns
flue sure reg number 648197
i have put up my old card. not to bothered about the front but i have put up the back for the details. mobile number and office are the same and the email has changed to dantapfixer@brevomail.net

Industry/Entity Type

Safety

Contact Information for Business Card

i do 24hr call outs
landlord safety checks
boiler breakdowns

Requirements
Must have
• i do 24hr call outs
• landlord safety checks
• all aspects of plumbing and heating
• boiler breakdowns
• flue sure reg number 648197

```html
<!DOCTYPE html>
<html lang="en">
<head>
<meta charset="utf-8">
<title>Hollins Plumbing &amp; Heating – Business Card</title>
<link rel="stylesheet" href="https://fonts.googleapis.com/css2?family=Lato:wght@400;700&display=swap">
<style>
  :root {
    --bg: #e9e4de;
    --card-white: #ffffff;
    --ink: #2b2b2b;
    --ink-soft: #3a3a3a;
    --brand-blue: #1e7bd0;
    --brand-red: #d8262f;
    --metal-light: #f4f5f6;
    --metal-mid: #dcdfe2;
    --badge-dark: #111111;
    --shadow: rgba(0, 0, 0, 0.18);
  }
  * { box-sizing: border-box; margin: 0; padding: 0; }
  html, body { width: 1200px; height: 1023px; overflow: hidden; }
  body {
    background: var(--bg);
    font-family: "Lato", sans-serif;
    color: var(--ink);
    position: relative;
  }
  .card {
    position: absolute;
    left: 280px;
    width: 640px;
    height: 366px;
    border-radius: 16px;
    box-shadow: 0 6px 18px var(--shadow);
    overflow: hidden;
  }
  .card-front { top: 100px; background: var(--card-white); }
  .card-back {
    top: 540px;
    background: linear-gradient(100deg, var(--metal-light) 0%, var(--metal-mid) 35%, var(--metal-light) 60%, var(--metal-mid) 100%);
  }

  /* wordmark */
  .wordmark {
    position: absolute;
    display: flex;
    align-items: center;
    gap: 12px;
    font-weight: 700;
    color: var(--ink);
    line-height: 1.05;
    text-transform: uppercase;
  }
  .wordmark-square {
    width: 34px; height: 34px;
    background: var(--brand-blue);
    flex: none;
  }
  .wordmark-name { font-size: 30px; letter-spacing: 0.5px; }
  .wordmark-name span { display: block; }
  .card-front .wordmark { top: 42px; right: 44px; }
  .card-back .wordmark { top: 44px; right: 44px; }

  /* front contact block */
  .contact {
    position: absolute;
    left: 44px;
    bottom: 40px;
  }
  .contact-name { font-size: 26px; font-weight: 700; color: var(--brand-blue); }
  .contact-role { font-size: 18px; color: var(--ink-soft); margin: 2px 0 12px; }
  .contact-list { list-style: none; font-size: 18px; color: var(--ink-soft); }
  .contact-list li { display: flex; align-items: center; gap: 10px; margin-bottom: 4px; }
  .contact-list svg { width: 14px; height: 14px; flex: none; fill: var(--brand-blue); }
  .contact-address { font-size: 18px; color: var(--ink-soft); margin-top: 10px; }

  /* back */
  .services {
    position: absolute;
    left: 44px;
    top: 150px;
    list-style: none;
    font-size: 18px;
    color: var(--ink);
    line-height: 1.45;
  }
  .divider {
    position: absolute;
    left: 44px;
    right: 44px;
    top: 132px;
    height: 2px;
    background: var(--brand-blue);
  }
  .registration {
    position: absolute;
    right: 44px;
    bottom: 36px;
    display: flex;
    align-items: center;
    gap: 16px;
  }
  .reg-text { font-size: 16px; color: var(--ink); }
  .reg-text strong { font-weight: 700; }
  .reg-badge {
    width: 96px; height: 96px;
    background: var(--badge-dark);
    border-radius: 4px;
  }
</style>
</head>
<body>

  <section class="card card-front" aria-label="Business card front">
    <div class="wordmark">
      <div class="wordmark-square"></div>
      <div class="wordmark-name"><span>Hollins</span><span>Plumbing &amp; Heating</span></div>
    </div>

    <div class="contact">
      <p class="contact-name">Owen Carrow</p>
      <p class="contact-role">President &amp; CEO</p>
      <ul class="contact-list">
        <li><svg viewBox="0 0 14 14" aria-hidden="true"><rect x="3" y="0.5" width="8" height="13" rx="1.5" fill="none" stroke="#1e7bd0" stroke-width="1.4"/></svg>07700 900418</li>
        <li><svg viewBox="0 0 14 14" aria-hidden="true"><path d="M3 1l2.5 0 1 3-1.5 1.2c.8 1.7 2 2.9 3.8 3.8L10 7.5l3 1V11c0 1-1 2-2 2C5.5 13 1 8.5 1 3c0-1 1-2 2-2z"/></svg>01632 960542</li>
        <li><svg viewBox="0 0 14 14" aria-hidden="true"><rect x="0.5" y="2.5" width="13" height="9" rx="1"/><path d="M1 3l6 5 6-5" fill="none" stroke="#fff" stroke-width="1.2"/></svg>dantapfixer@brevomail.net</li>
      </ul>
      <p class="contact-address">14 Marlow Rd, Kestwick, KT9 2RB</p>
    </div>
  </section>

  <section class="card card-back" aria-label="Business card back">
    <div class="wordmark">
      <div class="wordmark-square"></div>
      <div class="wordmark-name"><span>Hollins</span><span>Plumbing &amp; Heating</span></div>
    </div>

    <div class="divider"></div>

    <ul class="services">
      <li>I do 24hr call outs</li>
      <li>Landlord safety checks</li>
      <li>All aspects of plumbing and heating</li>
      <li>Boiler breakdowns</li>
    </ul>

    <div class="registration">
      <p class="reg-text">flue sure reg number <strong>648197</strong></p>
      <div class="reg-badge" role="img" aria-label="Registration badge"></div>
    </div>
  </section>

</body>
</html>
```